Aged Care Consultancy Business needs a business card design

I need a two sided business card - I want it clean and professional. Surprise me

Target Market(s)

middle aged and ageing victorians

Industry/Entity Type

Health Care

Contact Information for Business Card

Text to be included

Logo
Aged Care Consulting Services
Professional, Reliable, Affordable

Tovan Brelsick
Director
0427 31 64 92 (larger)
1300 73 29 41
tovan@wadolire.com.au
www.wadolcare.com.au
Facebook (details TBA)

include little icons beside the contact info:

- Envelope = email
- Phone = phone
- Globe = website

Font styles to use
Serif
Sans Serif

Requirements
Must have
• look proffesional and clean

```html
<!DOCTYPE html>
<html lang="en">
<head>
<meta charset="utf-8">
<title>Wadol Care – Business Card</title>
<link href="https://fonts.googleapis.com/css2?family=Open+Sans:wght@400;600;700&display=swap" rel="stylesheet">
<style>
  :root {
    --navy: #1b3f7c;
    --orange: #e8951d;
    --ink: #1c1c1c;
    --card: #ffffff;
    --ground: #ececec;
    --faint: #f1f1f1;
  }
  * { box-sizing: border-box; margin: 0; padding: 0; }
  html, body { width: 1200px; height: 1000px; overflow: hidden; }
  body {
    background: var(--ground);
    font-family: "Open Sans", Arial, sans-serif;
    color: var(--ink);
    position: relative;
  }
  .card {
    position: absolute;
    left: 265px;
    width: 665px;
    height: 397px;
    background: var(--card);
    border-radius: 24px;
    box-shadow: 0 4px 14px rgba(0,0,0,0.18);
    overflow: hidden;
  }
  .card--front { top: 73px; }
  .card--back { top: 533px; }

  .brand-name {
    font-family: "Open Sans", Arial, sans-serif;
    font-weight: 700;
    color: var(--navy);
    white-space: nowrap;
    letter-spacing: -0.5px;
  }
  .brand-dot {
    position: absolute;
    border-radius: 50%;
    background: var(--orange);
  }

  /* front */
  .front-brand { position: absolute; left: 32px; top: 128px; font-size: 46px; line-height: 1; }
  .front-brand-dot { left: 88px; top: 36px; width: 70px; height: 70px; }
  .faint-circle {
    position: absolute; left: 342px; top: 155px;
    width: 220px; height: 220px; border-radius: 50%;
    border: 38px solid var(--faint);
  }
  .contact-list { position: absolute; left: 32px; top: 262px; list-style: none; }
  .contact-list li { display: flex; align-items: center; gap: 6px; font-size: 16.5px; height: 23.5px; }
  .contact-list li.contact--main { font-size: 21px; height: 32px; margin-bottom: 4px; }
  .contact-list svg { width: 15px; height: 15px; fill: var(--navy); flex: none; }
  .contact--main svg { width: 19px; height: 19px; }

  .person { position: absolute; right: 32px; top: 207px; text-align: right; }
  .person-name { font-size: 21px; font-weight: 700; color: var(--navy); letter-spacing: 0.3px; line-height: 1.2; }
  .person-role { font-size: 15px; line-height: 1.2; }
  .social { position: absolute; right: 32px; top: 321px; display: flex; align-items: center; gap: 7px; font-size: 16px; }
  .social-mark { width: 11px; height: 14px; background: var(--navy); }
  .service { position: absolute; right: 32px; top: 349px; font-size: 16px; }

  /* back */
  .back-brand-dot { left: 272px; top: 92px; width: 120px; height: 120px; }
  .back-brand {
    position: absolute; left: 0; right: 0; top: 238px;
    text-align: center; font-size: 64px; line-height: 1;
  }
  .tagline { position: absolute; left: 0; right: 0; top: 347px; text-align: center; font-size: 16px; }
</style>
</head>
<body>

<section class="card card--front">
  <div class="brand-dot front-brand-dot"></div>
  <div class="brand-name front-brand">wadol care</div>
  <div class="faint-circle"></div>

  <ul class="contact-list">
    <li class="contact--main">
      <svg viewBox="0 0 24 24"><path d="M6.6 10.8a15.1 15.1 0 0 0 6.6 6.6l2.2-2.2c.3-.3.7-.4 1-.2 1.1.4 2.3.6 3.6.6.6 0 1 .4 1 1V20c0 .6-.4 1-1 1A17 17 0 0 1 3 4c0-.6.4-1 1-1h3.5c.6 0 1 .4 1 1 0 1.3.2 2.5.6 3.6.1.3 0 .7-.2 1z"/></svg>
      0427 31 64 92
    </li>
    <li>
      <svg viewBox="0 0 24 24"><path d="M2 9c2-4 18-4 20 0l-1 3h-4l-1-3H8l-1 3H3z"/><path d="M6 13h12l2 7H4z"/></svg>
      1300 73 29 41
    </li>
    <li>
      <svg viewBox="0 0 24 24"><path d="M2 5h20v14H2z M3 6l9 7 9-7" fill="var(--navy)"/><path d="M3 6.5l9 6.5 9-6.5" fill="none" stroke="#fff" stroke-width="1.6"/></svg>
      tovan@wadolire.com.au
    </li>
    <li>
      <svg viewBox="0 0 24 24"><circle cx="12" cy="12" r="10"/><path d="M2 12h20M12 2c3 3 3 17 0 20M12 2c-3 3-3 17 0 20" fill="none" stroke="#fff" stroke-width="1.4"/></svg>
      www.wadolcare.com.au
    </li>
  </ul>

  <div class="person">
    <div class="person-name">TOVAN BRELSICK</div>
    <div class="person-role">Director</div>
  </div>
  <div class="social">/wadolcarecentre <span class="social-mark"></span></div>
  <div class="service">Aged Care Consulting Services</div>
</section>

<section class="card card--back">
  <div class="brand-dot back-brand-dot"></div>
  <div class="brand-name back-brand">wadol care</div>
  <div class="tagline">Professional, Reliable, Affordable</div>
</section>

</body>
</html>
```